Letterhead and Envelopes design using existing logo. Logo can be found at tqvanholt.com

Use existing logo (attached) and incorporate in letterhead and envelope designs.

Current logo can be viewed at tqvanholt.com the web site reflect various parent and sub companies. Please see attached as well.

Target Market(s)

Other oil and gas operators.

Industry/Entity Type

Oil And Gas

Font styles to use
Sans Serif

Colors

Designer to choose colors to be used in the design.

Requirements
Must have
• Current logo and address
Nice to have
• Modern, contemporary approach yet incorporate existing traditional design.
• After design is selected for Wexford Tiller Holdings I will use similar design for Royalties, Exploration, Energy and Farms with different color schemes.

```html
<!DOCTYPE html>
<html lang="en">
<head>
<meta charset="utf-8">
<title>Wexford Tiller Holdings – Letterhead</title>
<link rel="stylesheet" href="https://fonts.googleapis.com/css2?family=Lato:wght@400;700&display=swap">
<style>
  :root{
    --backdrop:#b4bccb;
    --paper:#ffffff;
    --ink-dark:#2a2826;
    --brand-green:#4f8a3b;
    --body-grey:#8a8a8a;
    --label-white:#ffffff;
    --signature-blue:#c9d3ef;
  }
  *{box-sizing:border-box;margin:0;padding:0}
  html,body{width:1200px;height:900px;overflow:hidden}
  body{background:var(--backdrop);font-family:"Lato",sans-serif;position:relative}

  .letterhead{position:absolute;left:300px;top:24px;width:600px;height:852px;background:var(--paper);
    box-shadow:0 8px 24px rgba(40,50,70,.25);overflow:hidden}

  .header-band{position:absolute;left:0;top:0;width:600px;height:70px}
  .web-pill{position:absolute;left:28px;top:12px;height:22px;padding:0 12px 0 8px;border:1px solid #8d8d8d;border-radius:11px;
    display:flex;align-items:center;gap:6px;color:var(--label-white);font-size:10px}
  .web-pill .dot{width:9px;height:9px;border-radius:50%;background:var(--brand-green)}

  .brand-mark{position:absolute;right:28px;top:40px;display:flex;align-items:center;gap:10px;
    background:var(--paper);padding:10px 12px;border-radius:6px}
  .brand-mark .circle{width:22px;height:22px;border-radius:50%;background:var(--ink-dark)}
  .brand-mark .name{font-size:17px;font-weight:700;color:var(--ink-dark);line-height:1.1;width:120px}

  .letter{position:absolute;left:70px;top:150px;width:460px;color:var(--body-grey);font-size:10px;line-height:1.45}
  .recipient{margin-bottom:18px}
  .date{margin-bottom:18px}
  .salutation{font-weight:700;color:#666;margin-bottom:14px}
  .letter p{margin-bottom:12px}
  .signature{width:80px;height:36px;margin:28px 0 6px;background:var(--signature-blue);border-radius:4px}

  .footer{position:absolute;left:0;bottom:0;width:600px;height:90px;background:var(--ink-dark)}
  .contact-strip{position:absolute;left:28px;top:10px;width:544px;height:30px;background:var(--brand-green);
    border-radius:0 0 10px 10px;display:flex;align-items:center;justify-content:space-between;padding:0 22px;
    color:var(--label-white);font-size:11px}
  .contact-strip span{display:flex;align-items:center;gap:6px}
  .contact-strip svg{width:10px;height:10px;fill:var(--label-white)}
  .postal{position:absolute;left:0;top:52px;width:600px;text-align:center;color:var(--label-white);font-size:11.5px}
</style>
</head>
<body>
  <main class="letterhead">
    <svg class="header-band" viewBox="0 0 600 70" aria-hidden="true">
      <path d="M0 0H600V20C420 18 250 22 130 36 70 43 30 48 0 50Z" fill="var(--ink-dark)"/>
    </svg>
    <div class="web-pill"><span class="dot"></span>www.tqvanholt.com</div>

    <div class="brand-mark">
      <span class="circle"></span>
      <span class="name">Wexford Tiller Holdings</span>
    </div>

    <section class="letter">
      <div class="recipient">Halden GmbH<br>Petra Vogel<br>Lindenweg 14<br>4051 Basel<br>Schweiz</div>
      <div class="date">San Francisco, March 26, 2016</div>
      <div class="salutation">Lorem Ipsum,</div>
      <p>Cras mattis consectetur purus sit amet fermentum. Etiam porta sem malesuada magna mollis euismod. Integer posuere erat a ante venenatis dapibus posuere velit aliquet. Cras justo odio, dapibus ac facilisis in, egestas eget quam. Aenean eu leo quam. Pellentesque ornare sem lacinia quam venenatis vestibulum.</p>
      <p>Vivamus sagittis lacus vel augue laoreet rutrum faucibus dolor auctor. Donec sed odio dui. Etiam porta sem malesuada magna mollis euismod. Morbi leo risus, porta ac consectetur ac, vestibulum at eros. Nullam id dolor id nibh ultricies vehicula ut id elit.</p>
      <p>Donec id elit non mi porta gravida at eget metus. Fusce dapibus, tellus ac cursus commodo, tortor mauris condimentum nibh, ut fermentum massa justo sit amet risus. Cras justo odio, dapibus ac facilisis in, egestas eget quam. Cum sociis natoque penatibus et magnis dis parturient montes, nascetur ridiculus mus.</p>
      <p>Cum sociis natoque penatibus et magnis dis parturient montes, nascetur ridiculus mus. Curabitur blandit tempus porttitor. Aenean lacinia bibendum nulla sed consectetur. Lorem ipsum dolor sit amet, consectetur adipiscing elit.</p>
      <div class="signature" role="img" aria-label="Handwritten signature of the sender"></div>
      <div class="sender">Marianne Holt<br>President</div>
    </section>

    <footer class="footer">
      <div class="contact-strip">
        <span>License Number: 1234567</span>
        <span><svg viewBox="0 0 10 10"><path d="M2 0.5l1.6 0 .8 2.2-1 .8a6 6 0 0 0 3.1 3.1l.8-1 2.2.8 0 1.6C9.5 9 8.8 9.6 8 9.5 4 9 1 6 .5 2 .4 1.2 1 .5 2 .5z"/></svg>(555) 014.2290</span>
        <span><svg viewBox="0 0 10 10"><path d="M0 2h10v6H0z M0 2l5 3.5L10 2" fill="none" stroke="#fff" stroke-width="1"/></svg>reception@tqvanholt.com</span>
      </div>
      <div class="postal">Wexford Tiller Holdings, LLC. PO Box 318 Millbrook, North Dakota 58790</div>
    </footer>
  </main>
</body>
</html>
```